www.kelvorn.com Creative Website Re-design

We are looking for multiple page designs for a client website (www.kelvorn.com). The primary demographic is high school teenagers preparing for college applications. We believe the demographic is slightly skewed to female. We're looking for Home page, Content type main page (for example "All Fiction" http://www.kelvorn.com/poetry/ main page would include filters to show Top Pages, Most discussed, newest etc.) User page that a content contributor could log in to see all their content, add content etc. (samples in mock ups loaded). finally an inner page for everything else.
Need to ensure there are applicable advertising spaces as per the current site.
We are looking for a fun teenage friendly design that is bright and cheerful.
Updates
Project Deadline Extended
Reason: I'm not happy with the quality of the submissions to date or the lack of submissions received. I'm hoping by extending the deadline I can find something that is workable.
Target Market(s)
high school students - primarily female - applying for college
Industry/Entity Type
Education
Number of Pages Required
4 page
Requirements
Must have
- fresh cheerful look - we need to include the ad banners & right side column similar to the current site. The sample mock up is missing those
Nice to have
- logo can be punched up

```html
<!DOCTYPE html>
<html lang="en">
<head>
<meta charset="utf-8">
<title>Kelvorn – Creative Work</title>
<link href="https://fonts.googleapis.com/css2?family=Open+Sans:wght@300;400;600;700;800&display=swap" rel="stylesheet">
<style>
:root{
  --purple:#7c3187;
  --purple-text:#7a2f86;
  --yellow:#f6b400;
  --bar:#2a2a2a;
  --bar-active:#474747;
  --page:#ebebeb;
  --card:#ffffff;
  --line:#ececec;
  --muted:#a4a4a4;
  --footer:#333333;
}
*{box-sizing:border-box;margin:0;padding:0}
html,body{width:691px;height:1200px;overflow:hidden}
body{position:relative;background:var(--page);font-family:"Open Sans",Arial,sans-serif;color:#444}

/* header */
.site-header{position:absolute;left:0;top:0;width:691px;height:56px;background:var(--purple)}
.brand{position:absolute;left:76px;top:9px;color:#fff}
.brand-name{font-size:22px;font-weight:300;letter-spacing:.3px;line-height:22px}
.brand-tag{font-size:4.4px;letter-spacing:.2px;margin-top:4px;opacity:.85}
.main-nav{position:absolute;top:27px;left:244px;display:flex;gap:15px;font-size:5.6px;color:#fff}
.main-nav .submit{color:var(--yellow)}
.bell{position:absolute;left:555px;top:18px;width:23px;height:23px;border-radius:50%;background:#2b2b2b;display:flex;align-items:center;justify-content:center}
.user-pic{position:absolute;left:591px;top:17px;width:24px;height:24px;border-radius:50%;background:linear-gradient(135deg,#f3d9b8,#d8a26e)}
.badge{position:absolute;width:8px;height:8px;border-radius:50%;background:#e0302c;color:#fff;font-size:4.5px;text-align:center;line-height:8px}

/* filter bar */
.filter-bar{position:absolute;left:0;top:56px;width:691px;height:22px;background:var(--bar)}
.filter{position:absolute;top:0;height:22px;color:#ddd;font-size:7.2px;line-height:22px;padding-left:9px}
.filter.active{background:var(--bar-active)}
.filter svg{position:absolute;right:7px;top:8px}
.keywords{position:absolute;left:394px;top:0;line-height:22px;font-size:7px;color:#8a8a8a}
.search-btn{position:absolute;left:550px;top:0;width:64px;height:22px;background:var(--yellow);color:#fff;font-size:6.5px;font-weight:700;display:flex;align-items:center;justify-content:center;gap:4px}

/* feed */
.feed-col{position:absolute;top:88px;width:118px;display:flex;flex-direction:column;gap:13px}
.col-1{left:76px}.col-2{left:205px}.col-3{left:333px}
.card{background:var(--card);height:var(--h);display:flex;flex-direction:column;box-shadow:0 0 1px rgba(0,0,0,.08)}
.thumb{height:78px;position:relative;flex:none}
.play{position:absolute;left:50%;top:50%;width:22px;height:22px;margin:-11px 0 0 -11px;border-radius:50%;background:#fff;display:flex;align-items:center;justify-content:center}
.play.ghost{background:rgba(255,255,255,.55)}
.author{height:40px;flex:none;display:flex;align-items:center;gap:6px;padding-left:10px;border-bottom:1px solid var(--line)}
.avatar{width:23px;height:23px;border-radius:50%;flex:none}
.av-a{background:linear-gradient(135deg,#b8957a,#6d4f3e)}
.av-b{background:linear-gradient(135deg,#f0d2b0,#c58e5f)}
.av-c{background:linear-gradient(135deg,#9a8a7e,#3f3532)}
.name{font-size:5.8px;color:var(--purple-text)}
.body{flex:1;min-height:0;overflow:hidden;padding:9px 10px 0}
.body h3{font-size:7.2px;font-weight:400;color:var(--purple-text);line-height:10.2px;margin-bottom:5px;letter-spacing:-.05px}
.body p{font-size:4.9px;line-height:9px;color:var(--muted);letter-spacing:-.05px}
.stats{height:22px;flex:none;border-top:1px solid var(--line);display:flex}
.stats span{flex:1;display:flex;align-items:center;justify-content:center;gap:3px;font-size:5.8px;color:var(--muted);border-left:1px solid var(--line)}
.stats span:first-child{border-left:0}
.stats svg{fill:#b5b5b5}

.img-flag{background:linear-gradient(90deg,#3e3e3e 0%,#bdbdbd 35%,#5a5a5a 65%,#262626 100%)}
.img-sketch{background:linear-gradient(180deg,#c7c2d9,#8d86ad)}
.img-quilt{background:linear-gradient(135deg,#5b78a8,#c9a173 50%,#d9c7a2)}
.img-rose{background:radial-gradient(circle at 45% 45%,#c8232b 0 14%,#c9c9c9 30%,#b0b0b0 100%)}
.img-fountain{background:linear-gradient(180deg,#8797a5,#c8d0d7 60%,#7c7d80)}
.img-study{background:linear-gradient(135deg,#2b2623,#8a6a59 50%,#c9b8a8)}
.img-anime{background:linear-gradient(135deg,#f2f2f4,#d9b8c0 55%,#b23b3b)}
.img-shoes{background:linear-gradient(180deg,#7d7d7d,#c2c2c2 60%,#d88ab0)}

/* sidebar */
.sidebar{position:absolute;left:460px;top:88px;width:155px}
.ad{position:absolute;left:0;width:155px;overflow:hidden;color:#fff}
.ad-contest{top:0;height:128px;background:#3aa3dd}
.ad-contest .mark{position:absolute;left:7px;top:8px;width:22px;height:21px;background:#fff}
.ad-contest h4{position:absolute;left:33px;top:5px;font-size:10px;font-weight:800;letter-spacing:-.1px}
.ad-contest .sub{position:absolute;left:33px;top:21px;font-size:4.8px;font-weight:600}
.books{position:absolute;left:18px;top:36px;display:flex;gap:6px}
.books i{display:block;width:33px;height:62px}
.ad-contest .prize{position:absolute;left:0;width:155px;top:102px;text-align:center;font-size:8px;font-weight:600}
.ad-contest .learn{position:absolute;left:18px;top:114px;width:119px;height:10px;background:#17609a;font-size:6.8px;font-weight:800;text-align:center;line-height:10px;border-top:1px solid #fff}
.ad-network{top:138px;height:128px;background:linear-gradient(160deg,#3c3457,#231d36 60%,#40365a)}
.ad-network h4{position:absolute;left:0;width:155px;top:20px;text-align:center;font-size:13px;font-weight:600;line-height:17px}
.ad-network .dot{position:absolute;left:69px;top:72px;width:17px;height:17px;border-radius:50%;background:#fff}
.ad-network .co{position:absolute;left:0;width:155px;top:99px;text-align:center;font-size:7px;font-weight:700;letter-spacing:.3px}
.ad-interview{top:276px;height:128px;background:linear-gradient(180deg,#e8ecf4,#8aa4d6 55%,#1c2e73 85%)}
.ad-interview .photo{position:absolute;left:6px;top:4px;width:60px;height:72px;border:3px solid #fff;background:linear-gradient(180deg,#8aa0c4,#e26d2a 60%,#b45520)}
.ad-interview .who{position:absolute;left:80px;top:14px;width:70px;text-align:center;color:#1a1a3a;font-size:16px;font-weight:300;line-height:17px}
.ad-interview .yrs{position:absolute;left:80px;top:55px;width:70px;text-align:center;color:#1a1a3a;font-size:9px}
.ad-interview .cta{position:absolute;left:0;top:94px;width:155px;text-align:center;font-size:10px;line-height:12px;letter-spacing:-.3px}

.side-title{position:absolute;left:0;font-size:14px;line-height:18px;font-weight:400;color:var(--purple-text)}
.feed-box{position:absolute;left:0;width:155px;background:#fff;padding:10px 12px;font-size:5.4px;color:#333;overflow:hidden}
.feed-box .scroll{position:absolute;right:2px;top:0;width:2px;height:34px;background:#c8c8c8}
.post-head{display:flex;gap:6px;align-items:center;margin-bottom:8px}
.post-head .logo-sq{width:17px;height:17px;background:#c58b32}
.post-head b{display:block;font-size:6.6px;font-weight:600}
.post-head small{font-size:5px;color:#888}
.post-text{line-height:8px;margin-bottom:4px}
.post-img{height:64px}
.img-stamp{background:linear-gradient(135deg,#dcdfe4,#aeb4bc 60%,#6f747c)}
.img-shadow{background:linear-gradient(135deg,#565656,#b9b9b9 45%,#3e3e3e)}
.link-title{font-size:7.6px;margin-top:6px}
.link-desc{font-size:4.8px;color:#555;margin-top:2px}
.link-src{font-size:4.4px;color:#888;margin-top:2px}
.post-actions{display:flex;gap:14px;margin-top:9px;font-size:5.2px;color:#666}
.embed-row{position:absolute;left:0;top:871px;width:155px;display:flex;justify-content:space-between;font-size:5.2px;color:#888}

/* footer */
.site-footer{position:absolute;left:0;top:1062px;width:691px;height:138px;background:var(--footer);color:#ccc}
.footer-ad{position:absolute;left:76px;top:32px;width:335px;height:42px;background:linear-gradient(90deg,#8f1616,#c52a1c 60%,#7a1212)}
.footer-ad .sq{position:absolute;left:3px;top:3px;width:34px;height:36px;background:#f3a21a}
.footer-ad .title{position:absolute;left:55px;top:2px;font-size:17px;font-weight:800;line-height:18px;color:#f4e6c8}
.footer-ad .person{position:absolute;left:214px;top:0;width:52px;height:42px;background:linear-gradient(180deg,#5a2a1f,#2a120d)}
.footer-ad .url{position:absolute;right:4px;bottom:3px;font-size:5.4px;color:#fff}
.copy{position:absolute;left:76px;top:88px;font-size:6.2px;line-height:13.6px}
.socials{position:absolute;left:204px;top:88px;display:flex;gap:5px}
.socials i{display:block;width:14px;height:14px;border-radius:50%;background:#4f6fa8}
.newsletter{position:absolute;left:490px;top:37px;width:125px}
.newsletter h5{font-size:12px;font-weight:600;color:#fff;letter-spacing:.2px}
.newsletter .email{margin-top:5px;height:23px;background:#fff;color:#444;font-size:7px;padding-left:8px;line-height:23px}
.newsletter .subscribe{margin-top:5px;width:56px;height:23px;background:var(--yellow);color:#333;font-size:6.6px;text-align:center;line-height:23px}
</style>
</head>
<body>
<svg width="0" height="0" style="position:absolute">
  <symbol id="i-heart" viewBox="0 0 10 9"><path d="M5 9 1 5a2.6 2.6 0 0 1 4-3.4A2.6 2.6 0 0 1 9 5Z"/></symbol>
  <symbol id="i-eye" viewBox="0 0 12 8"><path d="M6 0C3 0 1 2.2 0 4c1 1.8 3 4 6 4s5-2.2 6-4C11 2.2 9 0 6 0Zm0 6.5A2.5 2.5 0 1 1 6 1.5a2.5 2.5 0 0 1 0 5Z"/><circle cx="6" cy="4" r="1.3"/></symbol>
  <symbol id="i-chat" viewBox="0 0 10 9"><path d="M1 0h8a1 1 0 0 1 1 1v5a1 1 0 0 1-1 1H4L1.5 9V7H1a1 1 0 0 1-1-1V1a1 1 0 0 1 1-1Z"/></symbol>
  <symbol id="i-caret" viewBox="0 0 8 5"><path d="M1 1l3 3 3-3" fill="none" stroke="#ddd" stroke-width="1.2"/></symbol>
</svg>

<header class="site-header">
  <div class="brand">
    <div class="brand-name">kelvorn</div>
    <div class="brand-tag">WRITE, DRAW, SHARE... SINCE 2004</div>
  </div>
  <nav class="main-nav">
    <span>Summer Programs</span><span>College Guide</span><span>Writing Courses</span><span>Get it in Print!</span><span class="submit">SUBMIT YOUR WORK</span>
  </nav>
  <div class="bell"><svg width="9" height="10" viewBox="0 0 9 10"><path d="M4.5 0C2.6 0 1.5 1.5 1.5 3.3V6L0 7.5h9L7.5 6V3.3C7.5 1.5 6.4 0 4.5 0ZM3.3 8.5a1.2 1.2 0 0 0 2.4 0Z" fill="#fff"/></svg></div>
  <span class="badge" style="left:552px;top:15px">1</span>
  <div class="user-pic" role="img" aria-label="Signed-in member avatar"></div>
  <span class="badge" style="left:589px;top:15px">1</span>
</header>

<div class="filter-bar">
  <div class="filter active" style="left:76px;width:104px">Creative Work<svg width="6" height="4"><use href="#i-caret"/></svg></div>
  <div class="filter" style="left:182px;width:106px">Most Inked<svg width="6" height="4"><use href="#i-caret"/></svg></div>
  <div class="filter" style="left:290px;width:96px">Following<svg width="6" height="4"><use href="#i-caret"/></svg></div>
  <div class="keywords">Additional Key Words...</div>
  <div class="search-btn"><svg width="6" height="6" viewBox="0 0 6 6"><circle cx="2.5" cy="2.5" r="1.8" fill="none" stroke="#fff" stroke-width=".9"/><path d="M3.8 3.8 5.6 5.6" stroke="#fff" stroke-width=".9"/></svg>SEARCH</div>
</div>

<main>
  <section class="feed-col col-1">
    <article class="card" style="--h:254px">
      <div class="thumb img-flag" role="img" aria-label="Black and white photo of a flag on a city building"></div>
      <div class="author"><span class="avatar av-a" role="img" aria-label="Contributor avatar"></span><span class="name">Evan Hale</span></div>
      <div class="body"><h3>Aliquam sed tincidunt diam, nec finibus</h3><p>Pellentesque non enim lacus. Donec faucibus felis lectus, a finibus nulla pretium vel. Sed egestas est non ligula feugiat, vitae laoreet velit mattis. Sed vulputate eros eu dapibus tempor. Fusce nisi magna, fringilla vel pharetra a, volutpat sed velit.</p></div>
      <div class="stats"><span><svg width="6" height="5"><use href="#i-heart"/></svg>82</span><span><svg width="7" height="5"><use href="#i-eye"/></svg>15</span><span><svg width="6" height="5"><use href="#i-chat"/></svg>51</span></div>
    </article>
    <article class="card" style="--h:134px">
      <div class="author"><span class="avatar av-b" role="img" aria-label="Contributor avatar"></span><span class="name">Evan Hale</span></div>
      <div class="body"><h3>Aliquam sed tincidunt diam, nec finibus</h3><p>Pellentesque non enim lacus. Donec faucibus felis lectus, a finibus nulla pretium vel. Sed egestas est non ligula feugiat, vitae laoreet velit mattis. Sed vulputate eros.</p></div>
      <div class="stats"><span><svg width="6" height="5"><use href="#i-heart"/></svg>82</span><span><svg width="7" height="5"><use href="#i-eye"/></svg>15</span><span><svg width="6" height="5"><use href="#i-chat"/></svg>51</span></div>
    </article>
    <article class="card" style="--h:253px">
      <div class="thumb img-fountain" role="img" aria-label="Photo of a person playing in a city fountain"><span class="play ghost"><svg width="7" height="8" viewBox="0 0 7 8"><path d="M0 0 7 4 0 8Z" fill="#fff"/></svg></span></div>
      <div class="author"><span class="avatar av-a" role="img" aria-label="Contributor avatar"></span><span class="name">Evan Hale</span></div>
      <div class="body"><h3>Aliquam sed tincidunt diam, nec finibus</h3><p>Pellentesque non enim lacus. Donec faucibus felis lectus, a finibus nulla pretium vel. Sed egestas est non ligula feugiat, vitae laoreet velit mattis. Sed vulputate eros. Suspendisse posuere vestibulum felis at</p></div>
      <div class="stats"><span><svg width="6" height="5"><use href="#i-heart"/></svg>82</span><span><svg width="7" height="5"><use href="#i-eye"/></svg>15</span><span><svg width="6" height="5"><use href="#i-chat"/></svg>51</span></div>
    </article>
    <article class="card" style="--h:254px">
      <div class="thumb img-shoes" role="img" aria-label="Photo of feet in pink sneakers"></div>
      <div class="author"><span class="avatar av-a" role="img" aria-label="Contributor avatar"></span><span class="name">Evan Hale</span></div>
      <div class="body"><h3>Aliquam sed tincidunt diam, nec finibus</h3><p>Pellentesque non enim lacus. Donec faucibus felis lectus, a finibus nulla pretium vel. Sed egestas est non ligula feugiat, vitae laoreet velit mattis. Sed vulputate eros eu dapibus tempor. Fusce nisi magna, fringilla vel pharetra a, volutpat sed velit.</p></div>
      <div class="stats"><span><svg width="6" height="5"><use href="#i-heart"/></svg>82</span><span><svg width="7" height="5"><use href="#i-eye"/></svg>15</span><span><svg width="6" height="5"><use href="#i-chat"/></svg>51</span></div>
    </article>
  </section>

  <section class="feed-col col-2">
    <article class="card" style="--h:176px">
      <div class="author"><span class="avatar av-b" role="img" aria-label="Contributor avatar"></span><span class="name">Evan Hale</span></div>
      <div class="body"><h3>Aliquam sed tincidunt diam, nec finibus</h3><p>Pellentesque non enim lacus. Donec faucibus felis lectus, a finibus nulla pretium vel. Sed egestas est non ligula feugiat, vitae laoreet velit mattis. Sed vulputate eros eu dapibus tempor. Fusce nisi magna, fringilla vel pharetra a, volutpat sed velit.</p></div>
      <div class="stats"><span><svg width="6" height="5"><use href="#i-heart"/></svg>82</span><span><svg width="7" height="5"><use href="#i-eye"/></svg>15</span><span><svg width="6" height="5"><use href="#i-chat"/></svg>51</span></div>
    </article>
    <article class="card" style="--h:253px">
      <div class="thumb img-quilt" role="img" aria-label="Painting with a star and patterned figure"><span class="play"><svg width="7" height="8" viewBox="0 0 7 8"><path d="M0 0 7 4 0 8Z" fill="#333"/></svg></span></div>
      <div class="author"><span class="avatar av-c" role="img" aria-label="Contributor avatar"></span><span class="name">Evan Hale</span></div>
      <div class="body"><h3>Aliquam sed tincidunt diam, nec finibus</h3><p>Pellentesque non enim lacus. Donec faucibus felis lectus, a finibus nulla pretium vel. Sed egestas est non ligula feugiat, vitae laoreet velit mattis. Sed vulputate eros. Suspendisse posuere vestibulum felis at</p></div>
      <div class="stats"><span><svg width="6" height="5"><use href="#i-heart"/></svg>82</span><span><svg width="7" height="5"><use href="#i-eye"/></svg>15</span><span><svg width="6" height="5"><use href="#i-chat"/></svg>51</span></div>
    </article>
    <article class="card" style="--h:216px">
      <div class="thumb img-study" role="img" aria-label="Photo of students studying at a table"></div>
      <div class="author"><span class="avatar av-b" role="img" aria-label="Contributor avatar"></span><span class="name">Evan Hale</span></div>
      <div class="body"><h3>Aliquam sed tincidunt diam, nec finibus</h3><p>Pellentesque non enim lacus. Donec faucibus felis lectus, a finibus nulla pretium vel.</p></div>
      <div class="stats"><span><svg width="6" height="5"><use href="#i-heart"/></svg>82</span><span><svg width="7" height="5"><use href="#i-eye"/></svg>15</span><span><svg width="6" height="5"><use href="#i-chat"/></svg>51</span></div>
    </article>
    <article class="card" style="--h:176px">
      <div class="author"><span class="avatar av-c" role="img" aria-label="Contributor avatar"></span><span class="name">Evan Hale</span></div>
      <div class="body"><h3>Aliquam sed tincidunt diam, nec finibus</h3><p>Pellentesque non enim lacus. Donec faucibus felis lectus, a finibus nulla pretium vel. Sed egestas est non ligula feugiat, vitae laoreet velit mattis. Sed vulputate eros eu dapibus tempor. Fusce nisi magna, fringilla vel pharetra a, volutpat sed velit.</p></div>
      <div class="stats"><span><svg width="6" height="5"><use href="#i-heart"/></svg>82</span><span><svg width="7" height="5"><use href="#i-eye"/></svg>15</span><span><svg width="6" height="5"><use href="#i-chat"/></svg>51</span></div>
    </article>
  </section>

  <section class="feed-col col-3">
    <article class="card" style="--h:234px">
      <div class="thumb img-sketch" role="img" aria-label="Pencil portrait drawing in violet tones"></div>
      <div class="author"><span class="avatar av-a" role="img" aria-label="Contributor avatar"></span><span class="name">Evan Hale</span></div>
      <div class="body"><h3>Aliquam sed tincidunt diam, nec finibus</h3><p>Pellentesque non enim lacus. Donec faucibus felis lectus, a finibus nulla pretium vel. Sed egestas est non ligula feugiat, vitae laoreet velit mattis. Sed vulputate eros.</p></div>
      <div class="stats"><span><svg width="6" height="5"><use href="#i-heart"/></svg>82</span><span><svg width="7" height="5"><use href="#i-eye"/></svg>15</span><span><svg width="6" height="5"><use href="#i-chat"/></svg>51</span></div>
    </article>
    <article class="card" style="--h:216px">
      <div class="thumb img-rose" role="img" aria-label="Photo of a red rose lying on sand"></div>
      <div class="author"><span class="avatar av-c" role="img" aria-label="Contributor avatar"></span><span class="name">Evan Hale</span></div>
      <div class="body"><h3>Aliquam sed tincidunt diam, nec finibus</h3><p>Pellentesque non enim lacus. Donec faucibus felis lectus, a finibus nulla pretium vel.</p></div>
      <div class="stats"><span><svg width="6" height="5"><use href="#i-heart"/></svg>82</span><span><svg width="7" height="5"><use href="#i-eye"/></svg>15</span><span><svg width="6" height="5"><use href="#i-chat"/></svg>51</span></div>
    </article>
    <article class="card" style="--h:157px">
      <div class="author"><span class="avatar av-b" role="img" aria-label="Contributor avatar"></span><span class="name">Evan Hale</span></div>
      <div class="body"><h3>Aliquam sed tincidunt diam, nec finibus</h3><p>Pellentesque non enim lacus. Donec faucibus felis lectus, a finibus nulla pretium vel. Sed egestas est non ligula feugiat, vitae laoreet velit mattis. Sed vulputate eros.</p></div>
      <div class="stats"><span><svg width="6" height="5"><use href="#i-heart"/></svg>82</span><span><svg width="7" height="5"><use href="#i-eye"/></svg>15</span><span><svg width="6" height="5"><use href="#i-chat"/></svg>51</span></div>
    </article>
    <article class="card" style="--h:238px">
      <div class="thumb img-anime" role="img" aria-label="Drawing of two winged characters"></div>
      <div class="author"><span class="avatar av-c" role="img" aria-label="Contributor avatar"></span><span class="name">Evan Hale</span></div>
      <div class="body"><h3>Aliquam sed tincidunt diam, nec finibus</h3><p>Pellentesque non enim lacus. Donec faucibus felis lectus, a finibus nulla pretium vel. Sed egestas est non ligula feugiat, vitae laoreet velit mattis. Sed vulputate eros.</p></div>
      <div class="stats"><span><svg width="6" height="5"><use href="#i-heart"/></svg>82</span><span><svg width="7" height="5"><use href="#i-eye"/></svg>15</span><span><svg width="6" height="5"><use href="#i-chat"/></svg>51</span></div>
    </article>
  </section>

  <aside class="sidebar">
    <div class="ad ad-contest">
      <span class="mark"></span>
      <h4>READ, WRITE, AND WIN!</h4>
      <div class="sub">ESSAY CONTESTS ON MARA VELL'S NOVELS</div>
      <div class="books" role="img" aria-label="Three novel covers">
        <i style="background:linear-gradient(180deg,#fbf4e4,#f2c23a)"></i>
        <i style="background:linear-gradient(180deg,#fff,#d43c36)"></i>
        <i style="background:linear-gradient(180deg,#fff,#3b7fc4)"></i>
      </div>
      <div class="prize">More Than $90,000 In Prizes.</div>
      <div class="learn">LEARN MORE</div>
    </div>

    <div class="ad ad-network" role="img" aria-label="Aerial city view at night">
      <h4>We’re the<br>connection</h4>
      <span class="dot"></span>
      <div class="co">ORVANE COMMUNICATIONS</div>
    </div>

    <div class="ad ad-interview">
      <div class="photo" role="img" aria-label="Portrait of an astronaut in an orange flight suit"></div>
      <div class="who">Walt<br>Brenner</div>
      <div class="yrs">(1934 - 2019)</div>
      <div class="cta">Read our exclusive interview<br>with Walt Brenner</div>
    </div>

    <h2 class="side-title" style="top:415px">Feedspace</h2>
    <div class="feed-box" style="top:438px;height:202px">
      <span class="scroll"></span>
      <div class="post-head"><span class="logo-sq"></span><div><b>Kelvorn Magazine</b><small>March 25 at 2:40am</small></div></div>
      <div class="post-text">Home as a Verb: Writers on Choosing to Live Overseas (via Stash) -</div>
      <div class="post-img img-stamp" role="img" aria-label="Passport page with a visa stamp"></div>
      <div class="link-title">Home as a Verb: Writers on C…</div>
      <div class="link-desc">Growing up all over the place makes you skill…</div>
      <div class="link-src">SAVELATER.COM</div>
      <div class="post-actions"><span>Like</span><span>Comment</span><span>Share</span></div>
    </div>

    <h2 class="side-title" style="top:655px">Chirper</h2>
    <div class="feed-box" style="top:678px;height:184px">
      <span class="scroll"></span>
      <div class="post-head"><span class="logo-sq"></span><div><b>Kelvorn</b><small>@kelvorn</small></div></div>
      <div class="post-text">Why We Love Star-Crossed Love Stories https://kelvornblog.blogpress.com/2016/11/01/why-we-love-star-cros sed-love-stories ...</div>
      <div class="post-img img-shadow" role="img" aria-label="Shadow of a couple on pavement" style="height:78px"></div>
      <div class="post-actions" style="color:#ccc"><span>♡</span><span>↦</span><span style="margin-left:auto">22h</span></div>
    </div>
    <div class="embed-row"><span>Embed</span><span>View on Chirper</span></div>
  </aside>
</main>

<footer class="site-footer">
  <div class="footer-ad">
    <span class="sq"></span>
    <div class="title">Five Years of<br>House Music</div>
    <div class="person" role="img" aria-label="Photo of a singer"></div>
    <div class="url">www.5lakeside.com</div>
  </div>
  <div class="copy">Copyright © 2017 Company name.<br>All rights reserved.</div>
  <div class="socials"><i></i><i style="background:#2a9bd8"></i><i style="background:#d63a2f"></i><i style="background:#5b7ea3"></i></div>
  <div class="newsletter">
    <h5>NEWSLETTER</h5>
    <div class="email">Email</div>
    <div class="subscribe">SUBSCRIBE</div>
  </div>
</footer>
</body>
</html>
```